lunch and dinne(al a carte) menus

we are a medium sized licenced club that has taken back the dining in the club
in the western suburbs of sydney working class with a rugby league base
our logo is a wolf kelford hawks

Reason: We have changed the name to Bluegate grill it could be done as Bluegate or Bluegate or Bluegate We need a lunch menu and a seperate dinner menu eg Bluegate grill l u n c h or Bluegate grill d i n n e r

Reason: Weve changed the name

Target Market(s)

young families, working class rugby leagues sporty types

Industry/Entity Type

Club

Requirements
Must have
• user friendly

```html
<!DOCTYPE html>
<html lang="en">
<head>
<meta charset="utf-8">
<title>Bluegate grill – Dinner Menu</title>
<link href="https://fonts.googleapis.com/css2?family=Oswald:wght@400;500;600&family=Cutive+Mono&display=swap" rel="stylesheet">
<style>
  :root{
    --frame:#ffffff;
    --board:#3b3b3d;
    --accent:#cfd83a;
    --ink:#f2f2f2;
    --muted:#d8d8d8;
  }
  *{margin:0;padding:0;box-sizing:border-box}
  html,body{width:721px;height:1200px;overflow:hidden;background:var(--frame)}
  .menu{
    position:absolute;left:12px;top:12px;width:697px;height:1176px;
    background:var(--board);color:var(--ink);
    font-family:"Oswald",sans-serif;
  }
  .brand{
    position:absolute;left:40px;top:46px;
    font-family:"Oswald",sans-serif;font-weight:600;font-size:46px;line-height:1;
    color:var(--accent);letter-spacing:1px;
  }
  .brand-rule{position:absolute;left:330px;right:0;top:94px;height:2px;background:var(--accent)}
  .menu-type{
    position:absolute;left:455px;top:62px;
    font-family:"Cutive Mono",monospace;font-size:26px;color:var(--accent);letter-spacing:1px;
  }
  .section-title{
    position:absolute;left:0;width:100%;top:226px;text-align:center;
    font-size:26px;font-weight:500;letter-spacing:1px;color:var(--ink);
  }
  .col-head{
    position:absolute;top:292px;font-size:11px;font-weight:500;letter-spacing:.5px;
  }
  .col-head.member{left:562px;color:var(--accent)}
  .col-head.visitor{left:625px;color:var(--ink)}
  .dish{position:absolute;left:45px;width:640px}
  .dish-name{font-size:16px;font-weight:500;line-height:20px;letter-spacing:.3px;text-transform:uppercase}
  .dish-desc{
    font-size:9.5px;line-height:11.5px;letter-spacing:.3px;color:var(--muted);
    text-transform:uppercase;width:330px;padding-left:14px;position:relative;
  }
  .dish-desc::before{content:"\25BA";position:absolute;left:0;top:0;font-size:9px}
  .price{position:absolute;top:0;font-size:17px;font-weight:500;line-height:20px}
  .price.member{left:520px;color:var(--accent)}
  .price.visitor{left:583px;color:var(--ink)}
  .footnote{
    position:absolute;left:0;width:100%;top:1112px;text-align:center;
    font-size:8.5px;letter-spacing:.4px;color:var(--muted);
  }
</style>
</head>
<body>
<main class="menu">
  <div class="brand">Bluegate grill</div>
  <div class="brand-rule"></div>
  <div class="menu-type">Dinner Menu</div>

  <h1 class="section-title">CHARGRILL</h1>
  <span class="col-head member">MEMBER</span>
  <span class="col-head visitor">VISITOR</span>

  <div class="dish" style="top:324px">
    <div class="dish-name">Mad Cow</div>
    <div class="dish-desc">A large tender rump topped with bug tail meat, calamari, scallops, prawns &amp; mussels all in a garlic white sauce</div>
    <span class="price member">$28</span><span class="price visitor">$30</span>
  </div>

  <div class="dish" style="top:382px">
    <div class="dish-name">BBQ</div>
    <div class="dish-desc">Massive rump steak cooked the way god intended it, with bacon melted cheddar, onion rings, corn kernels and beetroot finished with a dollop of sour cream</div>
    <span class="price member">$28</span><span class="price visitor">$30</span>
  </div>

  <div class="dish" style="top:490px">
    <div class="dish-name">Club Special</div>
    <div class="dish-desc">Scotch fillet steak cooked with love, topped with fried bacon fanned avocado melted camembert cheese with the sauce of your choice</div>
    <span class="price member">$28</span><span class="price visitor">$30</span>
  </div>

  <div class="dish" style="top:557px">
    <div class="dish-name">Surf &amp; Turf</div>
    <div class="dish-desc">Tender scotch fillet steak topped with large tiger prawns in a creamy garlic sauce</div>
    <span class="price member">$28</span><span class="price visitor">$30</span>
  </div>

  <div class="dish" style="top:620px">
    <div class="dish-name">House Steak</div>
    <div class="dish-desc">Huge rump steak topped with fanned avocado, melted cheese &amp; button mushroom sauce</div>
    <span class="price member">$28</span><span class="price visitor">$30</span>
  </div>

  <div class="dish" style="top:684px">
    <div class="dish-name">The Full House</div>
    <div class="dish-desc">A massive T-bone steak topped with a special seafood mix of prawns, calamari, mussels, scallops etc. with a spicy tomato &amp; basil sauce</div>
    <span class="price member">$28</span><span class="price visitor">$30</span>
  </div>

  <div class="dish" style="top:766px">
    <div class="dish-name">Cattlemans Steak</div>
    <div class="dish-desc">300g rib eye steak on the bone</div>
    <span class="price member">$28</span><span class="price visitor">$30</span>
  </div>

  <div class="dish" style="top:821px">
    <div class="dish-name">BBQ American Pork Ribs</div>
    <div class="dish-desc">Hickory smoked pork ribs, roasted in a BBQ sauce</div>
    <span class="price member">$28</span><span class="price visitor">$30</span>
  </div>

  <div class="dish" style="top:882px">
    <div class="dish-name">Rib Combo 1</div>
    <div class="dish-desc">Hickory smoked pork ribs, with char grilled chicken breast</div>
    <span class="price member">$28</span><span class="price visitor">$30</span>
  </div>

  <div class="dish" style="top:937px">
    <div class="dish-name">Rib Combo 2</div>
    <div class="dish-desc">Hickory smoked pork ribs, with char grilled rump steak</div>
    <span class="price member">$28</span><span class="price visitor">$30</span>
  </div>

  <div class="dish" style="top:994px">
    <div class="dish-name">Veal or Chicken Snitzel</div>
    <span class="price member">$20</span><span class="price visitor">$22</span>
  </div>

  <div class="dish" style="top:1032px">
    <div class="dish-name">Mixed Grill</div>
    <span class="price member">$20</span><span class="price visitor">$22</span>
  </div>

  <div class="dish" style="top:1068px">
    <div class="dish-name">Rump Steak 200g</div>
    <span class="price member">$20</span><span class="price visitor">$22</span>
  </div>

  <p class="footnote">* ALL MAIN MEALS ARE SERVED WITH CHIPS &amp; SALAD OR MASHED POTATO &amp; VEGETABLES *</p>
</main>
</body>
</html>
```